Sorlen cards

I want a simple business card that pops.
Logo on one side.
On side two i want.
"Are you thinking about a new building on your property, or renovating an existing structure? Contact".....
Owners Name: Dale Whitcombe
Owners Phone number: 717-555-0192
Address:4716 Oxtail Ridge RD, Bedford, PA 15522
Committed to Quality, Service, and Integrity

```html
<!DOCTYPE html>
<html lang="en">
<head>
<meta charset="utf-8">
<title>Sorlen Builders LLC — Business Card</title>
<link href="https://fonts.googleapis.com/css2?family=Work+Sans:wght@400;600;700&display=swap" rel="stylesheet">
<style>
  :root {
    --bg-top: #cfcfcd;
    --bg-mid: #8c8a86;
    --bg-bottom: #48453f;
    --card: #ffffff;
    --brand-brown: #43301d;
    --text-brown: #3b2c1f;
    --ink: #111111;
  }
  * { margin: 0; padding: 0; box-sizing: border-box; }
  html, body { width: 1200px; height: 1200px; overflow: hidden; }
  body {
    position: relative;
    background: linear-gradient(to bottom, var(--bg-top) 0%, var(--bg-mid) 50%, var(--bg-bottom) 100%);
    font-family: "Work Sans", Arial, sans-serif;
  }
  .card {
    position: absolute;
    left: 180px;
    width: 840px;
    height: 478px;
    background: var(--card);
    text-align: center;
  }
  .card--front { top: 104px; }
  .card--back { top: 618px; }

  .brand-mark {
    position: absolute;
    left: 372px;
    top: 118px;
    width: 96px;
    height: 96px;
    background: var(--brand-brown);
  }
  .brand-name {
    position: absolute;
    left: 0;
    right: 0;
    top: 240px;
    font-weight: 700;
    font-size: 50px;
    letter-spacing: 1px;
    line-height: 1;
    color: var(--brand-brown);
  }

  .back-content {
    position: absolute;
    left: 0;
    right: 0;
    top: 66px;
    color: var(--text-brown);
  }
  .pitch {
    font-size: 25px;
    font-weight: 400;
    line-height: 32px;
    letter-spacing: 0.6px;
  }
  .owner-name {
    margin-top: 28px;
    font-size: 34px;
    font-weight: 600;
    line-height: 36px;
    color: var(--ink);
    letter-spacing: 0.3px;
  }
  .owner-phone {
    font-size: 27px;
    line-height: 30px;
    color: var(--ink);
    letter-spacing: 1px;
  }
  .address {
    margin-top: 36px;
    font-size: 27px;
    line-height: 30px;
    letter-spacing: 0.8px;
  }
  .tagline {
    margin-top: 38px;
    font-size: 22px;
    font-weight: 700;
    line-height: 26px;
    color: var(--ink);
    letter-spacing: 0.3px;
  }
</style>
</head>
<body>
  <section class="card card--front" aria-label="Card front">
    <div class="brand-mark" aria-hidden="true"></div>
    <h1 class="brand-name">Sorlen Builders LLC</h1>
  </section>

  <section class="card card--back" aria-label="Card back">
    <div class="back-content">
      <p class="pitch">Are you thinking about a new building<br>on your property,<br>or renovating an existing structure?</p>
      <p class="owner-name">Dale Whitcombe</p>
      <p class="owner-phone">717 555 0192</p>
      <p class="address">4716 Oxtail Ridge RD, Bedford, PA 15522</p>
      <p class="tagline">Committed to Quality, Service, and Integrity</p>
    </div>
  </section>
</body>
</html>
```